"Dental Meadow" clinic needs brochure

a creative design is needed for flyer for a dental clinic, all info available on this website www.dentalmeadow-sample.ae, new imagery needed.

Industry/Entity Type

Clinic

```html
<!DOCTYPE html>
<html lang="en">
<head>
<meta charset="utf-8">
<title>Dental Meadow Clinic – Flyer</title>
<link rel="stylesheet" href="https://fonts.googleapis.com/css2?family=Open+Sans:wght@600;700&family=Cinzel:wght@700&display=swap">
<style>
  :root{
    --teal:#1d6e68;
    --teal-dark:#0f4a42;
    --grey:#8d8c91;
    --white:#ffffff;
    --page:#f2f2f2;
    --ink:#1b1b1b;
  }
  *{margin:0;padding:0;box-sizing:border-box}
  html,body{width:1200px;height:1200px;overflow:hidden;background:var(--page)}
  .flyer{
    position:absolute;left:200px;top:32px;width:800px;height:1136px;
    background:var(--white);overflow:hidden;
    font-family:"Open Sans",Arial,sans-serif;font-weight:600;color:var(--white);
  }
  .backdrop{position:absolute;left:0;top:0}
  .brand{
    position:absolute;left:0;top:76px;width:800px;
    display:flex;align-items:center;justify-content:center;gap:20px;
  }
  .brand-dot{width:42px;height:42px;border:4px solid var(--grey);border-radius:50%}
  .brand-name{
    font-family:"Open Sans",Arial,sans-serif;font-weight:700;
    font-size:44px;letter-spacing:3px;color:var(--teal);text-transform:uppercase;
  }
  .hours{
    position:absolute;left:506px;top:198px;width:284px;height:80px;
    background:var(--teal);text-align:center;padding-top:4px;
  }
  .hours h2{font-size:20px;letter-spacing:2px;font-weight:700;line-height:24px}
  .hours p{font-size:13.5px;letter-spacing:1px;font-weight:700;line-height:27px}
  .hours-fold{position:absolute;left:790px;top:198px}
  .photo{position:absolute;border-radius:50%;border:4px solid var(--white)}
  .photo-smile-open{left:38px;top:204px;width:207px;height:207px;
    background:radial-gradient(circle at 40% 50%,#f2d6cc,#e9b9a8 60%,#d8a597)}
  .photo-exam{left:266px;top:266px;width:270px;height:270px;
    background:radial-gradient(circle at 55% 50%,#e07a70,#f0c3ae 55%,#c9a489)}
  .photo-smile{left:572px;top:318px;width:195px;height:195px;
    background:radial-gradient(circle at 45% 50%,#f4ddd3,#e8bda9 60%,#d7a592)}
  .services{position:absolute;left:36px;top:546px;width:370px;line-height:27px}
  .section-title{font-family:"Cinzel",Georgia,serif;font-weight:700;font-size:30px;letter-spacing:2px;line-height:32px}
  .services .section-title{padding-left:8px}
  .group-title{font-size:17px;font-weight:700;letter-spacing:1.5px;text-align:center;padding-left:38px}
  .list{list-style:none}
  .list li{font-size:14.5px;letter-spacing:1.2px;padding-left:14px;position:relative}
  .list li::before{content:"";position:absolute;left:2px;top:12px;width:5px;height:5px;border-radius:50%;background:var(--white)}
  .extras{position:absolute;left:406px;top:558px;width:370px;line-height:27px}
  .extras .group-title{padding-left:0;text-align:left;margin-left:60px}
  .extras .group-title.second{margin-left:68px}
  .extras .list li{padding-left:16px}
  .about{position:absolute;left:412px;top:718px;width:370px;line-height:27px}
  .about .section-title{margin-left:58px}
  .about p{font-size:14.5px;letter-spacing:1.1px;white-space:nowrap}
  .contact{position:absolute;left:0;top:1081px;width:800px;height:55px;color:var(--ink);font-size:14.5px;letter-spacing:1px}
  .contact-line{position:absolute;display:flex;align-items:center;gap:10px;white-space:nowrap}
  .address{left:26px;top:6px}
  .phone{left:218px;top:31px}
  .social{left:437px;top:31px}
  .social-box{width:16px;height:16px;background:var(--ink);border-radius:3px}
</style>
</head>
<body>
<main class="flyer">
  <svg class="backdrop" width="800" height="1136" viewBox="0 0 800 1136">
    <defs>
      <linearGradient id="greyBand" x1="0" y1="0" x2="0" y2="1">
        <stop offset="0" stop-color="#e6e6e8"/>
        <stop offset="1" stop-color="#77767c"/>
      </linearGradient>
      <linearGradient id="tealBand" x1="0" y1="0" x2="0" y2="1">
        <stop offset="0" stop-color="#24a08d"/>
        <stop offset="0.45" stop-color="#1a7a6c"/>
        <stop offset="1" stop-color="#0f4a42"/>
      </linearGradient>
    </defs>
    <polygon points="0,307 300,404 300,472 0,532" fill="url(#greyBand)"/>
    <polygon points="0,532 800,368 800,1081 0,1081" fill="url(#tealBand)"/>
  </svg>

  <header class="brand">
    <span class="brand-dot"></span>
    <span class="brand-name">Dental Meadow Clinic</span>
  </header>

  <section class="hours">
    <h2>OPENING HOURS</h2>
    <p>Saturday - Sunday 11AM - 8PM</p>
    <p>Thursday 11Am - 4PM</p>
  </section>
  <svg class="hours-fold" width="10" height="94" viewBox="0 0 10 94">
    <polygon points="0,0 10,10 10,94 0,80" fill="var(--teal-dark)"/>
  </svg>

  <div class="photo photo-smile-open" role="img" aria-label="Close-up photo of an open, healthy smile"></div>
  <div class="photo photo-exam" role="img" aria-label="Photo of a dental mirror examining a patient's teeth"></div>
  <div class="photo photo-smile" role="img" aria-label="Close-up photo of a bright smile"></div>

  <section class="services">
    <h2 class="section-title">OUR SERVICES</h2>
    <h3 class="group-title">General Dentistry</h3>
    <ul class="list">
      <li>Scalling and Polishing</li>
      <li>White fillings</li>
      <li>Root canal Treatment</li>
      <li>Extraction</li>
      <li>Inlays and onlays</li>
      <li>Surgical Removal Teeth</li>
    </ul>
    <h3 class="group-title">Cosmetic Dentisry</h3>
    <ul class="list">
      <li>Veneers (Hollywood smile)</li>
      <li>Smile design</li>
      <li>Lumera Crowns</li>
      <li>Brightline Bleaching</li>
    </ul>
    <h3 class="group-title">Pediatric Dentistry</h3>
    <ul class="list">
      <li>White fillings</li>
      <li>Flouride treatment</li>
      <li>Pulpotomy and pulpectomy</li>
      <li>Extraction</li>
      <li>Special maintainer and Zircon crowns</li>
    </ul>
  </section>

  <section class="extras">
    <h3 class="group-title">Emergency Dentistry</h3>
    <h3 class="group-title second">Biologica Dentistry</h3>
    <ul class="list">
      <li>Safe Removal of Amalgam Filling<br>(SMART)</li>
      <li>Note: All our materials Bio-compatible<br>Materials</li>
    </ul>
  </section>

  <section class="about">
    <h2 class="section-title">ABOUT US</h2>
    <p>We are a dental practice devoted to<br>restoring and enhancing the natural<br>beauty of your smile using conservati-<br>ve, state-of-the-art procedures that<br>will result in beautiful, long lasting<br>smiles.</p>
    <p>A standard of excellence in personali-<br>zed dental care services our patients<br>deserve. We provide comprehensive<br>treatment planning and use restorative<br>and cosmetic dentistry to achieve your<br>optimal dental health.</p>
  </section>

  <footer class="contact">
    <div class="contact-line address">
      <svg width="20" height="18" viewBox="0 0 20 18"><path d="M10 1 L19 9 H16 V17 H12 V12 H8 V17 H4 V9 H1 Z" fill="var(--ink)"/></svg>
      <span>Suite 210, Palm Grove Street, Opp City Park, Abu Dhabi.</span>
    </div>
    <div class="contact-line phone">
      <svg width="22" height="16" viewBox="0 0 22 16"><path d="M2 6 C2 2 20 2 20 6 L17 8 L15 5 H7 L5 8 Z M6 9 H16 L19 15 H3 Z" fill="var(--ink)"/><circle cx="11" cy="12" r="2" fill="var(--white)"/></svg>
      <span>+971 2 555 0148</span>
    </div>
    <div class="contact-line social">
      <span class="social-box"></span>
      <span>@dentalmeadow</span>
    </div>
  </footer>
</main>
</body>
</html>
```